Fahrzeugaufbereitung inkl. Hol- und Bringedienst
Zielgruppe
Für Privatkunden
Aufgabenstellung
Benötige einen Flyer, um Privatkunden unseren neuen Hol- und Bringedienst für Fahrzeugaufbereitung vorzustellen.
Text und Preise unter www.lemar-transfer.de unter Fahrzeugaufbereitung.
Format Din Lang (105x210mm), zweiseitig

```html
<!DOCTYPE html>
<html lang="de">
<head>
<meta charset="utf-8">
<title>LEMAR Fahrzeugaufbereitung – Flyer DIN lang</title>
<link rel="stylesheet" href="https://fonts.googleapis.com/css2?family=Roboto+Condensed:wght@300;400;700&family=Anton&display=swap">
<style>
  :root{
    --stage:#d9d9d9;
    --ink:#000;
    --orange:#f08a2c;
    --blue:#3fa7e1;
    --white:#fff;
    --photo-light:#8a8d90;
    --photo-dark:#3a3c3e;
  }
  *{box-sizing:border-box;margin:0;padding:0}
  html,body{width:1200px;height:1139px;overflow:hidden}
  body{background:var(--stage);position:relative;font-family:"Roboto Condensed",sans-serif;color:var(--white)}
  .flyer{position:absolute;left:158px;width:884px;height:441px;background:var(--ink);overflow:hidden;box-shadow:0 4px 14px rgba(0,0,0,.35)}
  .flyer--front{top:70px}
  .flyer--back{top:600px}
  .top-rule{position:absolute;left:0;top:0;width:100%;height:8px;background:var(--orange)}
  .photo{position:absolute;left:0;top:8px;width:100%;height:232px;
    background:linear-gradient(90deg,var(--photo-dark) 0%,var(--photo-light) 22%,#b9bcbe 35%,var(--photo-dark) 50%,var(--photo-light) 72%,#b9bcbe 85%,var(--photo-dark) 100%)}
  .photo-band{position:absolute;left:0;top:166px;width:100%;height:74px;background:rgba(0,0,0,.6)}
  .headline{position:absolute;font-weight:700;color:var(--orange);letter-spacing:-.5px;line-height:1}
  .flyer--front .headline{left:36px;top:176px;font-size:72px}
  .flyer--back .headline{left:43px;top:170px;font-size:76px}
  .subline{position:absolute;left:182px;top:266px;font-size:46px;font-weight:300;line-height:1}
  .subline-icon{position:absolute;left:158px;top:284px}
  .badge{position:absolute;width:130px;height:130px}
  .badge svg{position:absolute;inset:0}
  .badge-text{position:absolute;inset:0;font-family:"Anton",sans-serif;color:var(--white);text-align:center;transform:rotate(-6deg)}
  .flyer--front .badge{left:732px;top:122px}
  .flyer--back .badge{left:708px;top:160px}
  .price-nur{position:absolute;left:22px;top:24px;font-size:20px}
  .price{position:absolute;left:14px;top:44px;font-size:38px;white-space:nowrap}
  .price small{font-size:16px}
  .price sup{font-size:18px;vertical-align:14px}
  .slogan{padding-top:24px;font-size:21px;line-height:1.15}
  .slogan strong{font-size:30px;font-weight:400}
  .fine-print{position:absolute;right:4px;top:150px;font-size:5px;color:#bbb;writing-mode:vertical-rl;transform:rotate(180deg)}
  .contact{position:absolute;top:377px;font-size:14px;line-height:18px}
  .contact--address{left:38px}
  .contact--address .company{color:var(--orange);font-weight:700}
  .contact--lines{left:182px}
  .contact--lines span{display:inline-block;width:34px}
  .brand{position:absolute;font-weight:700;color:var(--blue);line-height:1;letter-spacing:2px}
  .flyer--front .brand{left:640px;top:340px;font-size:74px}
  .flyer--back .brand{left:640px;top:345px;font-size:74px}
  .body-copy{position:absolute;left:43px;top:262px;width:255px;font-size:14px;line-height:17px;text-align:justify}
  .call-to-action{position:absolute;left:43px;top:410px;font-size:14px;font-weight:700;color:var(--orange)}
  .services{position:absolute;left:360px;top:268px;font-size:14px;line-height:18px}
  .services h2{font-size:14px;font-weight:700;color:var(--orange)}
  .services ul{list-style:none}
  .services li::before{content:"· "}
  .web{position:absolute;left:360px;top:412px;font-size:14px;font-weight:700;color:var(--orange)}
</style>
</head>
<body>

<section class="flyer flyer--front">
  <div class="top-rule"></div>
  <div class="photo" role="img" aria-label="Foto von oben: weißes Cabrio wird von drei Mitarbeitern gereinigt und poliert"></div>
  <div class="photo-band"></div>
  <h1 class="headline">Fahrzeugaufbereitung</h1>
  <svg class="subline-icon" width="18" height="20" viewBox="0 0 18 20" aria-hidden="true">
    <path d="M2 5h10l-3-3M2 5" stroke="var(--orange)" stroke-width="3" fill="none"/>
    <path d="M16 14H6l3 3" stroke="var(--blue)" stroke-width="3" fill="none"/>
  </svg>
  <p class="subline">inkl. Hol- und Bringedienst</p>
  <div class="badge">
    <svg viewBox="0 0 130 130" aria-hidden="true">
      <g fill="var(--blue)">
        <rect x="22" y="22" width="86" height="86"/>
        <rect x="22" y="22" width="86" height="86" transform="rotate(22.5 65 65)"/>
        <rect x="22" y="22" width="86" height="86" transform="rotate(45 65 65)"/>
        <rect x="22" y="22" width="86" height="86" transform="rotate(67.5 65 65)"/>
      </g>
    </svg>
    <div class="badge-text">
      <span class="price-nur">nur</span>
      <span class="price"><small>€</small> 59,<sup>90*</sup></span>
    </div>
  </div>
  <p class="fine-print">* Preise inkl. MwSt. und Anfahrt</p>
  <address class="contact contact--address" style="font-style:normal">
    <div class="company">L.E.M.A.R. GmbH</div>
    <div>Lindenweg 27</div>
    <div>10115 Berlin</div>
  </address>
  <div class="contact contact--lines">
    <div><span>Tel.:</span> 030 55 01 23 4 -0</div>
    <div><span>Mail:</span> info@lemar-transfer.de</div>
    <div><span>Web:</span> www.lemar-transfer.de</div>
  </div>
  <div class="brand">LEMAR</div>
</section>

<section class="flyer flyer--back">
  <div class="top-rule"></div>
  <div class="photo" role="img" aria-label="Foto von oben: weißes Cabrio wird von Mitarbeitern gewaschen und poliert"></div>
  <div class="photo-band"></div>
  <h1 class="headline">Fahrzeugservices</h1>
  <p class="body-copy">Wir bieten Ihnen eine klassische Fahrzeugaufbereitung inkl. Hol- und Bringedienst in Berlin und München für nur 59,90 € * an.<br>Sparen Sie Ihre wertvolle Zeit und lassen Sie Ihr Fahrzeug von uns an Ihrem Wunschort abholen und innerhalb der nächsten 90 Minuten aufbereiten.</p>
  <p class="call-to-action">Vereinbaren Sie noch heute einen Termin!</p>
  <div class="services">
    <h2>Unser Leitungsangebot enthält:</h2>
    <ul>
      <li>Hol- und Bringeservice</li>
      <li>Aussenwäsche inkl. Felgenreinigung</li>
      <li>Innenreinigung inkl. Cockpit und Saugen</li>
      <li>Fensterreinigung innen &amp; aussen</li>
      <li>Öl-, Wasser- und Wischwasserkontrolle</li>
      <li>Reifendruck und Profilkontrolle</li>
    </ul>
  </div>
  <p class="web">www.lemar-transfer.de</p>
  <div class="badge">
    <svg viewBox="0 0 130 130" aria-hidden="true">
      <g fill="var(--blue)">
        <rect x="22" y="22" width="86" height="86"/>
        <rect x="22" y="22" width="86" height="86" transform="rotate(22.5 65 65)"/>
        <rect x="22" y="22" width="86" height="86" transform="rotate(45 65 65)"/>
        <rect x="22" y="22" width="86" height="86" transform="rotate(67.5 65 65)"/>
      </g>
    </svg>
    <div class="badge-text slogan">Ihr Auto<br>wie<br><strong>NEU</strong></div>
  </div>
  <p class="fine-print">* Preise inkl. MwSt. und Anfahrt</p>
  <div class="brand">LEMAR</div>
</section>

</body>
</html>
```